HollowbrookJoinery (Custom Interior Trim work & Millwork Division)

HollowbrookJoinery

Cabinetry & Interior Finish

We are a custom millwork shop and fabricate cabinets, mantles, media rooms, bookcases, cabinet doors, dovetail draws, etc.

Also specialize in interior finish work (crown molding, trim work, staircases, installing kitchens, etc.

In the 2nd image only use if you can get the light fixture out of the picture thank you

please visit my web sites to get more pics and ideas.

you can copy and paste text and pics

www.qmaplerinc.example

www.hollowbrookjoinery.example

I like the color green tied into this project somehow

Shop

Serif

9bcb3c
ffffff
000000

• needs to be professional
• look and feel correct
• I added colors I would like to see but please feel free to add and be creative
• thank you
• Phone number
• email
• pics
• A picture of myself
• go to my website and copy it
• www.hollowbrookjoinery.example
• If this comes out right I will award the winner a web page design for my company

```html
<!DOCTYPE html>
<html lang="en">
<head>
<meta charset="utf-8">
<title>HollowbrookJoinery — Brochure</title>
<link rel="stylesheet" href="https://fonts.googleapis.com/css2?family=Open+Sans:wght@400;600;700&display=swap">
<style>
  :root {
    --green: #8cc63f;
    --charcoal: #58585a;
    --ink: #3a3a3a;
    --text: #2b2b2b;
    --rule: #b9b9b9;
    --paper: #ffffff;
    --backdrop: #e6e6e6;
    --wood-light: #c9a27a;
    --wood-dark: #5a3e2c;
  }
  * { box-sizing: border-box; margin: 0; padding: 0; }
  html, body { width: 1200px; height: 900px; overflow: hidden; }
  body {
    background: var(--backdrop);
    font-family: "Open Sans", Arial, sans-serif;
    color: var(--text);
    position: relative;
  }
  .panel {
    position: absolute;
    background: var(--paper);
    box-shadow: 0 6px 18px rgba(0,0,0,0.12);
  }

  /* Cover */
  .cover { left: 330px; top: 20px; width: 540px; height: 400px; }
  .brand { position: absolute; left: 26px; top: 26px; display: flex; align-items: center; gap: 12px; }
  .brand-mark { width: 34px; height: 34px; background: var(--green); }
  .brand-name { font-size: 20px; font-weight: 600; color: var(--ink); letter-spacing: 0.5px; line-height: 1.1; }
  .brand-tagline { font-size: 13px; color: var(--ink); }
  .cover-rule { position: absolute; left: 0; right: 0; height: 2px; background: var(--rule); }
  .cover-rule.top { top: 84px; }
  .cover-rule.bottom { top: 300px; }
  .cover-block { position: absolute; left: 0; top: 96px; width: 92px; height: 192px; background: var(--charcoal); }
  .cover-photo {
    position: absolute; left: 102px; top: 96px; width: 438px; height: 192px;
    background: linear-gradient(135deg, #6f6a62 0%, var(--wood-light) 45%, #a57c55 70%, #8e8a83 100%);
  }
  .cover-url { position: absolute; right: 26px; bottom: 34px; font-size: 14px; font-weight: 600; color: var(--text); }

  /* Inside spread */
  .spread { left: 60px; top: 460px; width: 1080px; height: 400px; }
  .fold { position: absolute; left: 540px; top: 0; bottom: 0; width: 1px; background: #dcdcdc; }
  .intro-rule { position: absolute; top: 0; bottom: 0; width: 1px; background: var(--rule); }
  .intro-rule.first { left: 28px; }
  .intro-rule.second { left: 44px; }
  .section-title { font-size: 24px; font-weight: 700; color: var(--charcoal); letter-spacing: 0.5px; }

  .intro { position: absolute; left: 90px; top: 40px; width: 420px; }
  .intro .section-title { margin-left: 150px; margin-bottom: 8px; }
  .intro-body { display: flex; gap: 16px; }
  .portrait-wrap { flex: 0 0 134px; }
  .portrait {
    width: 134px; height: 150px;
    background: radial-gradient(circle at 50% 40%, #9fd28d 0%, #7aa873 35%, #3a3a3a 100%);
  }
  .portrait-caption { font-size: 11px; color: #777; margin-top: 4px; }
  .intro-text p { font-size: 11.5px; line-height: 1.45; margin-bottom: 9px; }

  .index { position: absolute; left: 560px; top: 0; width: 520px; height: 400px; }
  .index-rule { position: absolute; left: 0; right: 0; height: 1px; background: var(--rule); }
  .index-rule.top { top: 86px; }
  .index-rule.bottom { top: 348px; }
  .index .section-title { position: absolute; left: 0; right: 0; top: 96px; text-align: center; }
  .categories { position: absolute; left: 18px; right: 18px; top: 134px; display: flex; gap: 6px; }
  .category { flex: 1; }
  .category-label {
    background: var(--green); color: var(--paper);
    font-size: 14px; font-weight: 600; text-transform: uppercase;
    text-align: center; padding: 3px 0; letter-spacing: 0.3px;
  }
  .category-photo { height: 166px; margin-top: 4px; }
  .category-photo.bookcases { background: linear-gradient(160deg, #c7c2b8 0%, var(--wood-dark) 40%, #3b2a20 100%); }
  .category-photo.bars { background: linear-gradient(170deg, #e8e2d4 0%, #d8cfbd 55%, #8a5a34 80%, #6e4527 100%); }
  .category-photo.doors { background: linear-gradient(180deg, #f1f1f1 0%, #d9dcdc 60%, #9c7a55 100%); }
</style>
</head>
<body>

  <section class="panel cover">
    <div class="brand">
      <div class="brand-mark"></div>
      <div>
        <div class="brand-name">HOLLOWBROOK JOINERY</div>
        <div class="brand-tagline">cabinetry &amp; interior finish</div>
      </div>
    </div>
    <div class="cover-rule top"></div>
    <div class="cover-block"></div>
    <div class="cover-photo" role="img" aria-label="Photo of a curved cherry media cabinet with drawer being built in the workshop"></div>
    <div class="cover-rule bottom"></div>
    <div class="cover-url">www.hollowbrookjoinery.example</div>
  </section>

  <section class="panel spread">
    <div class="intro-rule first"></div>
    <div class="intro-rule second"></div>

    <div class="intro">
      <h2 class="section-title">INTRO</h2>
      <div class="intro-body">
        <div class="portrait-wrap">
          <div class="portrait" role="img" aria-label="Portrait of the owner in a green shirt holding a drill"></div>
          <div class="portrait-caption">Dale Hartwell</div>
        </div>
        <div class="intro-text">
          <p>We have been doing all sorts of quality carpentry, woodworking and built-ins around Millbrook for a number of years. We know that homeowners want quality and great value.</p>
          <p>We also know that this is a rare combination, so we decided to show some of our work on this site and invite you to contact us for a free estimate.</p>
          <p>If you have a spot in the house that deserves some special treatment, we can help.</p>
          <p>Get affordable custom built-ins for your home. You'll be thrilled with the results.</p>
        </div>
      </div>
    </div>

    <div class="fold"></div>

    <div class="index">
      <div class="index-rule top"></div>
      <h2 class="section-title">INDEX</h2>
      <div class="categories">
        <div class="category">
          <div class="category-label">Bookcases</div>
          <div class="category-photo bookcases" role="img" aria-label="Photo of dark wood built-in bookcases"></div>
        </div>
        <div class="category">
          <div class="category-label">Bars, Desks, Media</div>
          <div class="category-photo bars" role="img" aria-label="Photo of a wood bar counter with a bowl of lemons"></div>
        </div>
        <div class="category">
          <div class="category-label">Doors &amp; Drawers</div>
          <div class="category-photo doors" role="img" aria-label="Photo of white cabinet doors and drawers"></div>
        </div>
      </div>
      <div class="index-rule bottom"></div>
    </div>
  </section>

</body>
</html>
```